Verdant Banner Design

We need 3 Banners for our superfood supplement e-commerce store.

1. Banner that advertises the food combining chart Dimensions 417 × 464 https://verdantlift.com/content/11-food-combining-rules

2. We need a banner that advertises our subscription program. (Dimensions 388 × 219)

3. We need a banner that highlights our ingredients. (Dimensions 388 × 215)

Our website: https://verdantlift.com/

1. The sizes are in dimensions.

2. Yes the banners are for our website, replacing the ones on the front page now https://verdantlift.com/

Content of Banners

1. Advertisng the food combining chart.

2. Advertising our Subscription program.

3 Advertising our ingredients.

Just use words like:

"Combine the right foods"

Target Market(s)

Organic Superfood Supplement

Contact Information for Business Card

The Business card has to be double sided and must have our logo

Colors

Designer to choose colors to be used in the design.

Requirements
Must have
• 1. You can use the attached images or not, it is up to you, please be creative.
• 2. Please provide the Raw AI files, and also give it in the following formats: JPEG, PNG,
• 3. I have added a file in the brief called subscription image please use to get an idea of the type of banner we are looking for, of course using our product images
Nice to have
• 1. Please show business card design as well, this will help us decide to choose you.
• 2. Please read the ingredients on the product itself, and if you can use some images for the ingredient banner that would be good.
• 3. The business card should have the following:
• Name: Brent Halloway
• Title: Co-Founder
• Address: Baldwin, NY
• Logo (see attached)
• Phone #: 877-555-0143
• Mobile #: 917-555-0188
• Email: info@verdantlift.com
• Website: www.verdantlift.com
Should not have
• No meat or dairy products in your images

```html
<!DOCTYPE html>
<html lang="en">
<head>
<meta charset="utf-8">
<title>Verdant – Combine the Right Foods</title>
<link href="https://fonts.googleapis.com/css2?family=Exo+2:wght@600&display=swap" rel="stylesheet">
<style>
  :root {
    --board-light: #f4f5f5;
    --board-mid: #e3e5e6;
    --ink: #050505;
    --orange-deep: #e8780e;
    --orange-bright: #f6a21d;
    --kiwi-deep: #5f9a1c;
    --kiwi-light: #b5d24a;
    --mark-white: rgba(255, 255, 255, 0.5);
    --mark-yellow: rgba(255, 214, 0, 0.72);
  }
  html, body {
    margin: 0;
    padding: 0;
    overflow: hidden;
  }
  .banner {
    position: relative;
    width: 1078px;
    height: 1200px;
    overflow: hidden;
    background: var(--board-light);
  }
  .wood-backdrop {
    position: absolute;
    inset: 0;
    background: linear-gradient(90deg, var(--board-light), var(--board-mid) 50%, var(--board-light));
  }
  .artwork {
    position: absolute;
    inset: 0;
  }
  .headline {
    position: absolute;
    left: 42px;
    top: 50px;
    margin: 0;
    font-family: "Exo 2", sans-serif;
    font-weight: 600;
    font-size: 182px;
    line-height: 156px;
    letter-spacing: -5px;
    white-space: nowrap;
    color: var(--ink);
  }
  .headline-line {
    display: block;
  }
</style>
</head>
<body>
  <div class="banner">
    <div class="wood-backdrop" role="img" aria-label="Whitewashed wooden planks background"></div>

    <svg class="artwork" width="1078" height="1200" viewBox="0 0 1078 1200">
      <defs>
        <radialGradient id="orangeFill" cx="0.25" cy="0.85" r="0.9">
          <stop offset="0" stop-color="var(--orange-deep)"/>
          <stop offset="1" stop-color="var(--orange-bright)"/>
        </radialGradient>
        <radialGradient id="kiwiFill" cx="0.6" cy="0.45" r="0.7">
          <stop offset="0" stop-color="#e9edc4"/>
          <stop offset="0.35" stop-color="var(--kiwi-light)"/>
          <stop offset="1" stop-color="var(--kiwi-deep)"/>
        </radialGradient>
        <clipPath id="orangeArea">
          <circle cx="-100" cy="1380" r="900"/>
        </clipPath>
        <path id="questionMark" d="M204,624 L204,480 C204,430 240,400 290,400 L800,400 C860,400 895,440 895,500 L895,600 C895,680 850,720 790,750 L700,795 C670,810 656,840 656,880 L656,990 C656,1006 645,1018 630,1018 L475,1018 C460,1018 448,1006 448,990 L448,880 C448,800 490,740 570,705 L640,675 C680,655 700,630 700,600 L700,560 C700,525 680,505 650,505 L440,505 C420,505 405,520 405,540 L405,600 C405,614 394,624 380,624 Z"/>
      </defs>

      <circle class="orange-slice" cx="-100" cy="1380" r="900" fill="url(#orangeFill)" role="img" aria-label="Halved orange seen from above"/>

      <path class="kiwi-slice" d="M640,600 C690,470 860,390 1078,384 L1078,1075 C960,1085 800,1070 700,1010 C640,960 650,880 680,820 C700,770 610,700 640,600 Z" fill="url(#kiwiFill)" role="img" aria-label="Halved kiwi fruit seen from above"/>

      <g class="question-mark">
        <use href="#questionMark" fill="var(--mark-white)"/>
        <use href="#questionMark" fill="var(--mark-yellow)" clip-path="url(#orangeArea)"/>
        <ellipse cx="552" cy="1120" rx="128" ry="48" fill="var(--mark-yellow)"/>
      </g>
    </svg>

    <h1 class="headline"><span class="headline-line">Combine the</span><span class="headline-line">Right Foods</span></h1>
  </div>
</body>
</html>
```